Children's writer business card design

I write children's mystery and adventure books for 9-12 year olds. My logo is a small robin redbreast bird which I will appear on all my commercial stationery and websites. I have a 'silhouette' of a bird on the mock up on your site and I like this, although your designers might make it look even better. The bird is non-negotiable!

When I tried to do the back of the card I got a hallmark. I don't like this.

I would like the card to be modern, 'clean' and striking. Not too much colour. Definitely the red for the bird so it really stands out.

Target Market(s)

parents and grandparents of children 9-12 years old, booksellers, teachers

Industry/Entity Type

Business

Contact Information for Business Card

I have created a rough design using Cardlyne which I hope you can access as this contains all of the information I want on my card.
The front has the following:
Maren Talbot
Writer & Education Consultant
www.marentalbotwriter.example

04915360284
mtalwex@quillmail.example

The back has:
Books
The Garnet Locket Puzzles (In bold)
The Riddle of the Garnet Locket (in italics)
The Whisper of the Garnet (italics)
The Pomfrey Project (in bold)
Book 1: Stuck (italics)
Book 2: Unstuck (italics)

I'm happy for you to change the design provided the 'robin' stays.
Thank you.

Colors
ec2027

Requirements
Must have
• the robin redbreast bird logo - although it is fine to change how the bird looks.
Should not have
• no watermark

```html
<!DOCTYPE html>
<html lang="en">
<head>
<meta charset="utf-8">
<title>Maren Talbot – Business Card</title>
<link rel="stylesheet" href="https://fonts.googleapis.com/css2?family=Archivo:wght@700&family=Open+Sans:ital,wght@0,400;0,700;1,400&family=Patrick+Hand&display=swap">
<style>
  :root {
    --backdrop: #2a2827;
    --card-white: #fbfbf9;
    --card-black: #070809;
    --ink: #111111;
    --paper-text: #f4f4f4;
    --robin-red: #ec2027;
  }
  html, body {
    margin: 0;
    padding: 0;
    width: 1200px;
    height: 930px;
    overflow: hidden;
    background: var(--backdrop);
  }
  .sheet {
    position: relative;
    width: 1200px;
    height: 930px;
    display: flex;
    align-items: center;
    justify-content: center;
    gap: 40px;
  }
  .card {
    position: relative;
    width: 540px;
    height: 309px;
    box-sizing: border-box;
    box-shadow: 0 6px 18px rgba(0,0,0,0.45);
  }

  /* Front face */
  .card--front {
    background: var(--card-white);
    color: var(--ink);
    text-align: center;
    padding-top: 46px;
  }
  .brand {
    display: inline-flex;
    align-items: flex-start;
    gap: 6px;
    font-family: "Archivo", "Helvetica Neue", Arial, sans-serif;
    font-weight: 700;
    font-size: 54px;
    letter-spacing: -1.5px;
    line-height: 1;
    margin: 0;
  }
  .brand__dot {
    width: 12px;
    height: 12px;
    border-radius: 50%;
    background: var(--robin-red);
    margin-top: 4px;
  }
  .tagline {
    font-family: "Patrick Hand", "Comic Sans MS", cursive;
    font-size: 23px;
    margin: 10px 0 0;
    letter-spacing: 0.3px;
  }
  .contact {
    list-style: none;
    margin: 42px 0 0;
    padding: 0;
    font-family: "Open Sans", Arial, sans-serif;
    font-size: 14.5px;
    line-height: 1.45;
  }

  /* Back face */
  .card--back {
    background: var(--card-black);
    color: var(--paper-text);
    font-family: "Open Sans", Arial, sans-serif;
    font-size: 14px;
  }
  .series {
    position: absolute;
    right: 230px;
    top: 86px;
    text-align: right;
    margin: 0;
  }
  .series p { margin: 0 0 10px; }
  .series .title-bold { font-weight: 700; }
  .series .title-italic { font-style: italic; }
  .series .title-bold--gap { margin-top: 24px; }
  .divider {
    position: absolute;
    left: 322px;
    top: 74px;
    width: 3px;
    height: 86px;
    background: var(--robin-red);
  }
  .volumes {
    position: absolute;
    left: 342px;
    top: 86px;
    margin: 0;
  }
  .volumes p { margin: 0 0 10px; font-style: italic; }
</style>
</head>
<body>
  <main class="sheet">
    <section class="card card--front" aria-label="Card front">
      <h1 class="brand">Maren Talbot<span class="brand__dot"></span></h1>
      <p class="tagline">Maren Talbot Writer &amp; Education Consultant</p>
      <ul class="contact">
        <li>04915360284</li>
        <li>mtalwex@quillmail.example</li>
        <li>www.marentalbotwriter.example</li>
      </ul>
    </section>

    <section class="card card--back" aria-label="Card back">
      <div class="series">
        <p class="title-bold">Books The Garnet Locket Puzzles</p>
        <p class="title-italic">The Riddle of the Garnet Locket</p>
        <p class="title-italic">The Whisper of the Garnet</p>
        <p class="title-bold title-bold--gap">The Pomfrey Project</p>
      </div>
      <span class="divider"></span>
      <div class="volumes">
        <p>Book 1: Stuck</p>
        <p>Book 2: Unstuck</p>
      </div>
    </section>
  </main>
</body>
</html>
```